Logo & Visitenkarte für Gesundheit
Zielgruppe
Gesundheitsprodukte
Ernährungsberatung
Aufgabenstellung
nicht spezifisch Logo mit Essen und Trinken. Eher ein allgemeines Logo für Gesundheit

```html
<!DOCTYPE html>
<html lang="de">
<head>
<meta charset="utf-8">
<title>Licht für den Alltag – Visitenkarten</title>
<link href="https://fonts.googleapis.com/css2?family=Roboto:wght@400;700&display=swap" rel="stylesheet">
<style>
:root{
  --bg:#e6e7e9;
  --card:#ffffff;
  --teal:#114a59;
  --green:#b5c31b;
  --white:#ffffff;
}
*{margin:0;padding:0;box-sizing:border-box}
html,body{width:1200px;height:750px;overflow:hidden;background:var(--bg);font-family:"Roboto",Arial,sans-serif}
.sheet{position:relative;width:1200px;height:750px}
.card{position:absolute;width:314px;height:203px;background:var(--card)}
.card--front-a{left:269px;top:143px}
.card--front-b{left:629px;top:143px}
.card--back-a{left:269px;top:411px}
.card--back-b{left:631px;top:411px}

.front-mark{position:absolute;left:0;right:0;top:30px;display:flex;flex-direction:column;align-items:center;gap:14px}
.front-mark .dot{width:52px;height:52px;border-radius:50%;background:var(--teal)}
.front-mark .brand{font-size:25px;line-height:28px;font-weight:700;color:var(--teal);text-align:center;letter-spacing:.6px}
.front-url{position:absolute;left:0;right:0;top:183px;text-align:center;font-size:8px;font-weight:700;color:var(--teal)}

.back-mark{position:absolute;right:16px;top:18px;display:flex;align-items:center;gap:8px}
.back-mark .dot{width:26px;height:26px;border-radius:50%;background:var(--teal)}
.back-mark .brand{font-size:16px;line-height:18px;font-weight:700;color:var(--teal);letter-spacing:.5px}

.person{position:absolute;left:16px;top:98px;color:var(--teal)}
.person .name{font-size:13.5px;font-weight:700;letter-spacing:.2px;line-height:16px}
.person .role{font-size:10.5px;line-height:12px}

.band{position:absolute;left:0;top:128px;width:314px;height:57px;background:var(--teal);color:var(--white);font-size:9.6px}
.address{position:absolute;left:16px;top:12px;line-height:13px}
.contacts{position:absolute;left:154px;top:6px;list-style:none}
.contacts li{display:flex;align-items:center;gap:8px;height:15px}
.contacts svg{width:12px;height:12px;flex:none}
</style>
</head>
<body>
<main class="sheet">

  <section class="card card--front-a">
    <div class="front-mark"><span class="dot"></span><span class="brand">LICHT FÜR<br>DEN ALLTAG</span></div>
    <p class="front-url">www.lichtfuerdenalltag.de</p>
  </section>

  <section class="card card--front-b">
    <div class="front-mark"><span class="dot"></span><span class="brand">LICHT 4<br>DEN ALLTAG</span></div>
    <p class="front-url">www.lichtfuerdenalltag.de</p>
  </section>

  <section class="card card--back-a">
    <div class="back-mark"><span class="dot"></span><span class="brand">LICHT FÜR<br>DEN ALLTAG</span></div>
    <div class="person"><p class="name">LENA BEISPIEL</p><p class="role">Function</p></div>
    <div class="band">
      <p class="address">Streetnumber 00<br>City name</p>
      <ul class="contacts">
        <li><svg viewBox="0 0 12 12"><path d="M8 1c1 0 1.5 1 1 2.5C8 7 6 10 3 11 2 11.3 1.5 10.5 2 10l1.5-1 1 .5C6 8 7 6 7 4.5L6.3 3.5 7 1z" fill="#fff"/></svg>000000000000</li>
        <li><svg viewBox="0 0 12 12"><rect x="1" y="2.5" width="10" height="7" fill="none" stroke="#fff" stroke-width="1.2"/><path d="M1 2.5l5 4 5-4M1 9.5l3.5-3.5M11 9.5L7.5 6" fill="none" stroke="#fff" stroke-width="1"/></svg>info@lichtfuerdenalltag.de</li>
        <li><svg viewBox="0 0 12 12"><circle cx="6" cy="6" r="5" fill="none" stroke="#fff"/><ellipse cx="6" cy="6" rx="2.2" ry="5" fill="none" stroke="#fff" stroke-width=".8"/><path d="M1 6h10M2 3.5h8M2 8.5h8" stroke="#fff" stroke-width=".8"/></svg>www.lichtfuerdenalltag.de</li>
      </ul>
    </div>
  </section>

  <section class="card card--back-b">
    <div class="back-mark"><span class="dot"></span><span class="brand">LICHT 4<br>DEN ALLTAG</span></div>
    <div class="person"><p class="name">LENA BEISPIEL</p><p class="role">Function</p></div>
    <div class="band">
      <p class="address">Streetnumber 00<br>City name</p>
      <ul class="contacts">
        <li><svg viewBox="0 0 12 12"><path d="M8 1c1 0 1.5 1 1 2.5C8 7 6 10 3 11 2 11.3 1.5 10.5 2 10l1.5-1 1 .5C6 8 7 6 7 4.5L6.3 3.5 7 1z" fill="#fff"/></svg>000000000000</li>
        <li><svg viewBox="0 0 12 12"><rect x="1" y="2.5" width="10" height="7" fill="none" stroke="#fff" stroke-width="1.2"/><path d="M1 2.5l5 4 5-4M1 9.5l3.5-3.5M11 9.5L7.5 6" fill="none" stroke="#fff" stroke-width="1"/></svg>info@lichtfuerdenalltag.de</li>
        <li><svg viewBox="0 0 12 12"><circle cx="6" cy="6" r="5" fill="none" stroke="#fff"/><ellipse cx="6" cy="6" rx="2.2" ry="5" fill="none" stroke="#fff" stroke-width=".8"/><path d="M1 6h10M2 3.5h8M2 8.5h8" stroke="#fff" stroke-width=".8"/></svg>www.lichtfuerdenalltag.de</li>
      </ul>
    </div>
  </section>

</main>
</body>
</html>
```